Letterhead for Kestrelbay Night Doctor

Now we have a new logo we need some letterhead. Attached is the new logo and also the information we need to have on it. We have not yet decided on colour but would like to see a version in each to assist in choosing. I have attached one of the logos but do not have high quality version of the other 'ORHCT member' logo. These can be less prominent. Also Kestrelbay Health Providers Collective Inc. can be less prominent perhaps small font stating "KND is trading name for the Kestrelbay Health Providers Collective Inc."

```html
<!DOCTYPE html>
<html lang="en">
<head>
<meta charset="utf-8">
<title>Kestrelbay Night Doctor – Letterhead</title>
<link href="https://fonts.googleapis.com/css2?family=Fira+Sans:wght@600&family=Open+Sans:wght@400;600;700&family=Questrial&display=swap" rel="stylesheet">
<style>
  :root {
    --backdrop: #3b3b3b;
    --paper: #ffffff;
    --ink: #333333;
    --red: #e31e2d;
    --grey-band: #6d6d6d;
    --green: #1f5a3c;
    --navy: #1f4e8c;
  }
  * { box-sizing: border-box; margin: 0; padding: 0; }
  html, body { width: 1200px; height: 1000px; overflow: hidden; }
  body { background: var(--backdrop); position: relative; font-family: "Open Sans", sans-serif; }

  .sheet {
    position: absolute; left: 270px; top: 70px; width: 668px; height: 864px;
    background: var(--paper); box-shadow: 3px 4px 8px rgba(0,0,0,.45); overflow: hidden;
  }
  .brand-dot { position: absolute; left: 46px; top: 44px; width: 44px; height: 44px; border-radius: 50%; background: var(--red); }
  .brand-name {
    position: absolute; left: 109px; top: 36px;
    font-family: "Fira Sans", sans-serif; font-weight: 600; color: var(--ink);
    font-size: 23px; line-height: 20px;
  }

  .trading { position: absolute; right: 187px; top: 56px; text-align: right; }
  .trading-label { font-size: 10px; color: #222; font-weight: 600; line-height: 13px; }
  .trading-company { font-size: 11.5px; color: var(--red); line-height: 15px; white-space: nowrap; }

  .member { position: absolute; left: 498px; top: 12px; width: 70px; }
  .member-mark { display: block; margin-left: 11px; width: 44px; height: 40px; background: var(--green); border-radius: 6px; }
  .member-label { font-size: 8.5px; font-weight: 700; color: #222; margin-top: 7px; white-space: nowrap; }
  .abn { position: absolute; left: 499px; top: 66px; font-size: 13px; font-weight: 700; color: #111; letter-spacing: .3px; white-space: nowrap; }
  .badge { position: absolute; left: 573px; top: 11px; width: 53px; height: 53px; border-radius: 50%; background: var(--navy); border: 3px solid #d9e2ef; }

  .rule { position: absolute; left: 215px; top: 86px; }

  .contacts {
    position: absolute; left: 236px; top: 95px; width: 404px; display: flex; justify-content: space-between;
    font-family: "Questrial", sans-serif; font-size: 9px; color: #222; white-space: nowrap;
  }
  .contacts span { display: flex; align-items: center; gap: 3px; }
  .contacts svg { width: 7px; height: 7px; fill: var(--red); }

  .footer-band { position: absolute; left: 0; top: 827px; width: 598px; height: 5px; background: var(--grey-band); }
  .footer-mark { position: absolute; left: 598px; top: 806px; width: 50px; height: 50px; border-radius: 50%; background: var(--grey-band); }
  .footer-address {
    position: absolute; left: 0; top: 839px; width: 668px; text-align: center;
    font-family: "Questrial", sans-serif; font-size: 11.5px; color: #222; letter-spacing: .1px;
  }
</style>
</head>
<body>
  <main class="sheet">
    <header>
      <span class="brand-dot"></span>
      <div class="brand-name">Kestrelbay<br>Night<br>Doctor</div>

      <div class="trading">
        <p class="trading-label">Trading name for</p>
        <p class="trading-company">Kestrelbay Health Providers Collective Inc.</p>
      </div>

      <div class="member">
        <span class="member-mark" role="img" aria-label="ORHCT member badge"></span>
        <p class="member-label">ORHCT MEMBER</p>
      </div>
      <p class="abn">ABN 48 903 512 667</p>
      <span class="badge" role="img" aria-label="Accreditation badge"></span>

      <svg class="rule" width="453" height="6" viewBox="0 0 453 6">
        <rect x="0" y="0" width="2" height="5" fill="#e31e2d"/>
        <rect x="4" y="0" width="2" height="5" fill="#e31e2d"/>
        <rect x="8" y="0" width="2" height="5" fill="#e31e2d"/>
        <rect x="12" y="0" width="2" height="5" fill="#e31e2d"/>
        <rect x="16" y="0" width="2" height="5" fill="#e31e2d"/>
        <rect x="22" y="1" width="431" height="3" fill="#e31e2d"/>
      </svg>

      <div class="contacts">
        <span><svg viewBox="0 0 10 10"><path d="M2 0h2l1 3-1.5 1a6 6 0 0 0 2.5 2.5L7 5l3 1v2a2 2 0 0 1-2 2A8 8 0 0 1 0 2a2 2 0 0 1 2-2z"/></svg>02 5550 1184</span>
        <span><svg viewBox="0 0 10 10"><rect x="2" y="0" width="6" height="3"/><rect x="0" y="3" width="10" height="5"/><rect x="2" y="7" width="6" height="3"/></svg>02 5550 1190</span>
        <span><svg viewBox="0 0 10 10"><rect x="0" y="2" width="10" height="7"/></svg>enquiries@kbdoctor.com.au</span>
        <span><svg viewBox="0 0 10 10"><circle cx="5" cy="5" r="5"/></svg>www.kbdoctor.com.au</span>
      </div>
    </header>

    <footer>
      <div class="footer-band"></div>
      <span class="footer-mark"></span>
      <p class="footer-address">4/18 Harlow Crescent, Kestrelbay NSW 2611 &#9679; PO Box 377, Ashgrove Point NSW 2614</p>
    </footer>
  </main>
</body>
</html>
```